Harbor Loan Ad (8 x 8)

Bluevale Financial Services
Introduces

THE HARBOR LOAN

Interest Rates as low as 2.5%
640 Minimum Credit Score
Close in Only 22 Days

$100 per loan donated to Open Doors Equity Movement

Call (800) 555-0147 Today
Bluevale Financial Services, Inc.
7200 Marrowfield Road, Corwin Falls, MD 21990
www.bluevaleonline.example
NMLS #718360

(small print)
Up to 95% Loan to Value. Owner Occupied Only. Purchase or Rate & Term Only. All loans subject to Underwriter Approval.

```html
<!DOCTYPE html>
<html lang="en">
<head>
<meta charset="utf-8">
<title>The Harbor Loan – Bluevale Financial Services</title>
<link rel="stylesheet" href="https://fonts.googleapis.com/css2?family=Oswald:wght@600&family=Montserrat:wght@300;400;500;600;700&display=swap">
<style>
  :root {
    --page: #ececec;
    --paper: #fbfbfb;
    --blue: #0b4fa2;
    --blue-deep: #073d84;
    --gold: #b6a032;
    --yellow: #dcc526;
    --ink: #222222;
    --white: #ffffff;
  }
  * { margin: 0; padding: 0; box-sizing: border-box; }
  html, body { width: 800px; height: 1200px; overflow: hidden; }
  body { background: var(--page); font-family: "Montserrat", Arial, sans-serif; position: relative; }

  .ad {
    position: absolute; left: 20px; top: 220px; width: 760px; height: 760px;
    background: var(--paper); overflow: hidden;
    box-shadow: 0 6px 14px rgba(0,0,0,0.28);
  }
  .ad-shapes { position: absolute; inset: 0; }

  .brand {
    position: absolute; top: 52px; left: 0; width: 100%;
    display: flex; justify-content: center; align-items: center; gap: 10px;
    font-weight: 600; font-size: 20px; color: var(--blue);
  }
  .brand-dot { width: 18px; height: 18px; border-radius: 50%; background: var(--gold); }

  .title-the, .title-loan, .title-name {
    position: absolute; left: 0; width: 100%; text-align: center; line-height: 1;
  }
  .title-the { top: 199px; font-weight: 300; font-size: 68px; color: var(--yellow); }
  .title-name {
    top: 250px; font-family: "Oswald", "Arial Narrow", sans-serif; font-weight: 600;
    font-size: 132px; color: var(--white); letter-spacing: 4px; line-height: 0.9;
  }
  .title-loan { top: 381px; font-weight: 300; font-size: 68px; color: var(--yellow); letter-spacing: 1px; }

  .feature { position: absolute; display: flex; gap: 10px; }
  .feature svg { width: 36px; height: 22px; margin-top: 6px; flex: none; }
  .feature-label { color: var(--white); font-weight: 300; font-size: 27px; line-height: 26px; }
  .feature-value { display: block; color: var(--yellow); font-weight: 700; font-size: 25px; line-height: 26px; }
  .feature-rates { left: 56px; top: 462px; }
  .feature-score { left: 56px; top: 538px; }
  .feature-close { left: 433px; top: 462px; }

  .donation {
    position: absolute; left: 433px; top: 531px; width: 273px; height: 66px;
    background: var(--yellow); border-radius: 8px;
    display: flex; align-items: center; padding-left: 15px; gap: 10px;
  }
  .donation-amount { font-weight: 700; font-size: 34px; color: var(--blue); }
  .donation-note { font-weight: 500; font-size: 11.5px; line-height: 14px; color: var(--blue-deep); white-space: nowrap; }

  .footer-company { position: absolute; left: 29px; top: 640px; font-weight: 700; font-size: 18px; color: var(--ink); }
  .footer-phone {
    position: absolute; left: 29px; top: 669px; display: flex; align-items: center; gap: 14px;
    font-weight: 700; font-size: 31px; color: var(--ink); letter-spacing: 0.5px;
  }
  .footer-phone svg { width: 26px; height: 26px; }
  .footer-address, .footer-web {
    position: absolute; left: 358px; display: flex; align-items: center; gap: 8px;
    font-weight: 600; font-size: 14px; color: var(--ink); white-space: nowrap;
  }
  .footer-address { top: 642px; }
  .footer-web { top: 677px; }
  .footer-web svg, .footer-address svg { width: 14px; height: 18px; }
  .footer-divider { color: var(--yellow); margin: 0 8px; font-weight: 400; }
  .footer-nmls { font-size: 11px; font-weight: 600; letter-spacing: 0.5px; }
  .fine-print { position: absolute; left: 29px; top: 716px; font-size: 9px; font-weight: 400; color: #333; }
  .housing-badge { position: absolute; left: 690px; top: 704px; width: 34px; height: 30px; border: 3px solid #555; border-radius: 3px; }
</style>
</head>
<body>
  <main class="ad">
    <svg class="ad-shapes" viewBox="0 0 760 760">
      <defs>
        <linearGradient id="photoTint" x1="0" y1="0" x2="0" y2="1">
          <stop offset="0" stop-color="#0c53a8"/>
          <stop offset="0.6" stop-color="#0a4b9b"/>
          <stop offset="1" stop-color="#0d4f9f"/>
        </linearGradient>
      </defs>
      <path role="img" aria-label="Blue-tinted photograph of a large two-storey house" d="M0,270 Q380,30 760,270 L760,614 L0,614 Z" fill="url(#photoTint)"/>
      <path d="M0,262 Q380,14 760,262 L760,270 Q380,30 0,270 Z" fill="var(--gold)"/>
      <rect x="0" y="616" width="760" height="6" fill="var(--gold)"/>
      <g class="title-frame" stroke="#ffffff" stroke-width="1.5" fill="none">
        <polyline points="313,232 129,232 129,406 266,406"/>
        <polyline points="456,232 631,232 631,406 496,406"/>
      </g>
      <g class="title-frame-dots" fill="#ffffff">
        <circle cx="313" cy="232" r="4"/><circle cx="456" cy="232" r="4"/>
        <circle cx="266" cy="406" r="4"/><circle cx="496" cy="406" r="4"/>
      </g>
    </svg>

    <header class="brand">
      <span class="brand-dot"></span>
      <span class="brand-name">Bluevale Financial Services</span>
    </header>

    <h1 class="title">
      <span class="title-the">THE</span>
      <span class="title-name">HARBOR</span>
      <span class="title-loan">LOAN</span>
    </h1>

    <div class="feature feature-rates">
      <svg viewBox="0 0 36 22"><polyline points="2,11 9,19 22,3" fill="none" stroke="#dcc526" stroke-width="3.5"/><polyline points="14,17 16,19 30,3" fill="none" stroke="#dcc526" stroke-width="3.5"/></svg>
      <p class="feature-label">Interest Rates as<span class="feature-value">low as 2.5%</span></p>
    </div>
    <div class="feature feature-score">
      <svg viewBox="0 0 36 22"><polyline points="2,11 9,19 22,3" fill="none" stroke="#dcc526" stroke-width="3.5"/><polyline points="14,17 16,19 30,3" fill="none" stroke="#dcc526" stroke-width="3.5"/></svg>
      <p class="feature-label">640 Minimum<span class="feature-value">Credit Score</span></p>
    </div>
    <div class="feature feature-close">
      <svg viewBox="0 0 36 22"><polyline points="2,11 9,19 22,3" fill="none" stroke="#dcc526" stroke-width="3.5"/><polyline points="14,17 16,19 30,3" fill="none" stroke="#dcc526" stroke-width="3.5"/></svg>
      <p class="feature-label">Close in Only<span class="feature-value">22 Days</span></p>
    </div>

    <div class="donation">
      <span class="donation-amount">$100</span>
      <span class="donation-note">Per loan donated to Open<br>Doors Equity Movement</span>
    </div>

    <footer>
      <p class="footer-company">Bluevale Financial Services, Inc</p>
      <p class="footer-phone">
        <svg viewBox="0 0 24 24"><path d="M6.6 2.5l3 3.6-2 2.3c1.2 2.8 3.2 4.9 6 6.1l2.3-2 3.6 3-1.8 3.6C10.5 19 4.9 13.4 3 6.3z" fill="#dcc526"/></svg>
        (800) 555-0147
      </p>
      <p class="footer-address">
        <svg viewBox="0 0 14 18"><path d="M7 1a6 6 0 0 0-6 6c0 4.5 6 10 6 10s6-5.5 6-10a6 6 0 0 0-6-6zm0 8.3A2.3 2.3 0 1 1 7 4.7a2.3 2.3 0 0 1 0 4.6z" fill="#dcc526"/></svg>
        7200 Marrowfield Road, Corwin Falls, MD 21990
      </p>
      <p class="footer-web">
        <svg viewBox="0 0 14 14"><circle cx="7" cy="7" r="6" fill="none" stroke="#dcc526" stroke-width="1.5"/><path d="M1 7h12M7 1c-3 3-3 9 0 12M7 1c3 3 3 9 0 12" fill="none" stroke="#dcc526" stroke-width="1.2"/></svg>
        www.bluevaleonline.example<span class="footer-divider">|</span><span class="footer-nmls">NMLS #718360</span>
      </p>
      <p class="fine-print">Up to 95% Loan to Value. Owner Occupied Only. Purchase or Rate &amp; Term Only. All loans subject to Underwriter Approval.</p>
      <span class="housing-badge" role="img" aria-label="Fair housing badge"></span>
    </footer>
  </main>
</body>
</html>
```